A5 & A3 Size flyer for OPEN NIGHT - Adult Education

We need a A5 & A3 formatted flyer for our upcoming OPEN NIGHT on Thursday, 17th November 2016 at our Blackburn campus. A3 for poster to display and A5 for flyers.

We are one of Victoria's leading private Reconised Training Organisations based in Melbourne, Victoria, Australia who specialise in the training of nationally recognised training courses in Pathology, Individual Support (Ageing, Home & Community, Disability), Allied Health Assistance, Health Services Assistance, Disability & Ageing Support.

The purpose of our open night is to gain prospective students for 2017 courses and the soul purpose of this flyer is to promote via emails, postal mail and hard copy drop offs to prospective clients, employers and our partnered networks for exposure.

The final design should reflect the colour scheme & style we have used in the attached already promoted designs. Should include our logo, address, event details, website and social media buttons (Facebook, Instagram, Youtube, Twitter, Pinterest & LinkedIn) Should be in line with our overall branding, as per our website www.brimcoveacademy.edu.au and ensure it is bold and engaging for promotional purposes.

Please also see our event listing for which ahs further information you may be able to use: https://bcaopenevening16.ticketnook.com.au

If you ahve any questions please send through a message!

Target Market(s)

Prospective students, employer organisations workforce

Industry/Entity Type

Adult

Colors
f37122
f78f20
ffc214
ffffff

Requirements
Must have
• See project description

```html
<!DOCTYPE html>
<html lang="en">
<head>
<meta charset="utf-8">
<title>Open Night – Brimcove Academy</title>
<link rel="stylesheet" href="https://fonts.googleapis.com/css2?family=Arvo:wght@700&family=Lato:ital,wght@0,400;0,900;1,400;1,700&family=Montserrat:wght@300;400;500&display=swap">
<style>
  :root {
    --orange-deep: #f37122;
    --orange: #f78f20;
    --yellow: #ffc214;
    --white: #ffffff;
    --ink: #1e1e1e;
    --backdrop: #d6d6d6;
    --photo-dark: #2a2a2c;
    --photo-mid: #6d6b6a;
  }
  * { box-sizing: border-box; margin: 0; padding: 0; }
  html, body { width: 1200px; height: 871px; overflow: hidden; }
  body {
    background: radial-gradient(ellipse at 50% 40%, #e6e6e6 0%, var(--backdrop) 100%);
    font-family: "Lato", sans-serif;
    position: relative;
  }
  .flyer {
    position: absolute;
    left: 306px; top: 20px;
    width: 588px; height: 831px;
    background: var(--white);
    box-shadow: 0 10px 30px rgba(0,0,0,.25);
    overflow: hidden;
  }
  .title-open {
    position: absolute; top: 36px; left: 0; right: 0; z-index: 3;
    display: flex; align-items: center; justify-content: center; gap: 14px;
    font-family: "Montserrat", sans-serif; font-weight: 400;
    font-size: 88px; line-height: 1; color: var(--ink); letter-spacing: -2px;
  }
  .title-open .dash { width: 46px; height: 7px; background: var(--orange-deep); }
  .title-night {
    position: absolute; top: 124px; left: 50%; transform: translateX(-50%);
    width: 360px; height: 92px; z-index: 3;
  }
  .title-night svg { position: absolute; inset: 0; }
  .title-night span {
    position: absolute; inset: 0; display: flex; align-items: center; justify-content: center;
    font-family: "Arvo", serif; font-weight: 700; font-size: 80px; line-height: 1;
    color: var(--orange-deep); letter-spacing: 2px;
  }
  .team-photo {
    position: absolute; top: 196px; left: 0; width: 100%; height: 380px;
    background:
      linear-gradient(to bottom, rgba(255,255,255,0) 50%, var(--white) 100%),
      radial-gradient(ellipse at 50% 40%, var(--photo-mid) 0%, var(--photo-dark) 60%, #4a4848 100%);
  }
  .brand {
    position: absolute; top: 470px; left: 0; right: 0; z-index: 2;
    display: flex; flex-direction: column; align-items: center; gap: 5px;
  }
  .brand .mark { width: 38px; height: 38px; border-radius: 50%; background: var(--orange-deep); }
  .brand .name { font-family: "Montserrat", sans-serif; font-weight: 500; font-size: 25px; line-height: 1.1; color: var(--orange-deep); }
  .brand .rto { font-size: 8px; color: #777; }
  .campus {
    position: absolute; top: 578px; left: 0; right: 0; text-align: center;
    font-weight: 900; font-size: 28px; line-height: 1.1; color: var(--ink); letter-spacing: .5px;
  }
  .date-ribbon { position: absolute; top: 628px; left: 0; width: 300px; height: 80px; }
  .date-ribbon svg { position: absolute; inset: 0; }
  .date-ribbon p {
    position: absolute; left: 26px; top: 6px; color: var(--white);
    font-family: "Montserrat", sans-serif; font-size: 26px; line-height: 1.08;
  }
  .contact { position: absolute; top: 722px; left: 26px; font-size: 19px; color: var(--ink); list-style: none; }
  .contact li { display: flex; align-items: center; gap: 8px; line-height: 1.35; }
  .contact svg { width: 14px; height: 14px; flex: none; }
  .divider {
    position: absolute; left: 318px; top: 632px; height: 160px;
    border-left: 2px dashed #555;
  }
  .follow { position: absolute; left: 334px; top: 628px; width: 240px; }
  .follow h2 {
    font-style: italic; font-weight: 700; font-size: 25px; line-height: 1.2; color: var(--yellow);
    text-align: center; letter-spacing: -.5px;
  }
  .socials { display: flex; justify-content: center; gap: 9px; margin-top: 8px; }
  .socials span { width: 28px; height: 28px; border-radius: 50%; }
  .socials span:nth-child(odd) { background: var(--orange-deep); }
  .socials span:nth-child(even) { background: var(--orange); }
  .courses { font-style: italic; font-size: 11px; line-height: 1.3; color: #333; margin-top: 10px; }
  .footer-band { position: absolute; bottom: 0; left: 0; width: 100%; height: 14px; background: var(--yellow); }
</style>
</head>
<body>
  <main class="flyer">
    <h1 class="title-open"><span class="dash"></span>OPEN<span class="dash"></span></h1>
    <div class="title-night">
      <svg viewBox="0 0 360 92" preserveAspectRatio="none" aria-hidden="true">
        <polygon points="0,6 360,6 344,46 360,86 0,86 16,46" fill="#ffc214"/>
      </svg>
      <span>NIGHT</span>
    </div>
    <div class="team-photo" role="img" aria-label="Group photo of the training staff in black uniform shirts"></div>
    <div class="brand">
      <span class="mark"></span>
      <span class="name">Brimcove Academy</span>
      <span class="rto">RTO ID 41207</span>
    </div>
    <h2 class="campus">BRIMCOVE ACADEMY BLACKBOM</h2>
    <div class="date-ribbon">
      <svg viewBox="0 0 300 80" preserveAspectRatio="none" aria-hidden="true">
        <polygon points="0,0 300,0 282,34 300,68 0,68" fill="#f37122"/>
        <polygon points="0,68 120,68 120,80 0,80" fill="#c8521a"/>
      </svg>
      <p>17 november,<br>2016, 5–8 pm</p>
    </div>
    <ul class="contact">
      <li><svg viewBox="0 0 14 14" aria-hidden="true"><rect x="1" y="1" width="12" height="12" rx="3" fill="#f37122"/><path d="M5 4 q-1 3 3 6 l1-1" stroke="#fff" stroke-width="1.6" fill="none"/></svg>03 5550 1842</li>
      <li><svg viewBox="0 0 14 14" aria-hidden="true"><circle cx="7" cy="7" r="6" fill="none" stroke="#f37122" stroke-width="1.4"/><path d="M1 7h12M7 1c-3 3-3 9 0 12M7 1c3 3 3 9 0 12" stroke="#f37122" fill="none"/></svg>www.ticketnook.com.au</li>
    </ul>
    <div class="divider"></div>
    <section class="follow">
      <h2>FOLLOW US:</h2>
      <div class="socials" role="img" aria-label="Social media buttons">
        <span></span><span></span><span></span><span></span><span></span><span></span>
      </div>
      <p class="courses">Pathology, Individual Support (Ageing, Home &amp; Community, Disability), Allied Health Assistance, Health Services Assistance, Disability &amp; Ageing Support.</p>
    </section>
    <div class="footer-band"></div>
  </main>
</body>
</html>
```